依頼概要
薬局内で製造・販売している薬のラベルシールの作成をお願いします。

■依頼の目的/概要
弊社は茨城県で調剤薬局を6店舗展開し、「いつもあなたのそばに」をモットーに、いつでも気軽に相談していただける薬局を目指して、業務を行っております。
このたび創業20周年を機に、薬局製剤ラベルのリニューアルを行います。
どうぞよろしくお願いします。

■依頼の詳細
内服薬3種類(かぜ薬、ビタミン剤、整腸剤)のラベルシールの作成

銀色のジップ付きアルミ袋にラベルを貼って販売しており、その形を継続します。
今までのイメージカラーを引き継ぎたいと考えております。
ラベルには商品名、効能、包数、のほかに各販売店舗名、法人名、住所を入れる必要があります。
テキストが編集できるような状態で納品ください。

【ラベルサイズ】
140mm×100mm

【デザインに対するイメージの希望】
あまり重厚な感じではなくて良いですが、お薬ですので、信頼感のある、効果があることがイメージできるものをお願いします。

■その他・参考事項
各商品の販売価格は、1200~1600円程度です。
現在の各商品のラベル等詳細についてはファイルに添付します。
イメージカラー等はそちらをご参考下さい。
ご提案頂いている皆様、ありがとうございます。
デザインいただくイメージとして販売ターゲット像をお示しします。

販売ターゲットは35歳女性。結婚し、8歳と1歳の二人の子供がいるが仕事もしており、自分のことは後回しになりがち。下の子供が風邪で病院にかかり薬局へ処方箋を持っていたところ、処方箋なしで買える薬局製剤を目にする。風邪気味で疲れもあった自分用に風邪薬とビタミンを買い、お腹をこわしやすい上の子供用に整腸剤も購入した。薬のデザインは癒し感があるし、風邪薬は夫が風邪気味の時にも使えるし、家庭の常備薬としても良いと思う。

初めに現在のラベルをお示ししてしまったので先入観が出てしまいがちであったかと思います。今後初めてご覧になる方は現在のラベルの写真を入れないファイルを添付いたしましたので、そちらをご覧ください。
どうぞよろしくお願いします。
■ 選んだ理由

白ベースでスッキリしたデザインに信頼感と薬の効果を感じました。
また、曲線のラインと、光が差し込んでいるような地の薄い斜めの模様から癒しも感じられ、こちらに決定させていただきました。

■ 提案者全員のお礼・コメント

多くの皆様にご参加いただき、誠にありがとうございました。
初めてのコンペであり不安がありましたが、数多くのご提案を頂きましたこと、感謝申し上げます。

```html
<!DOCTYPE html>
<html lang="ja">
<head>
<meta charset="utf-8">
<title>整腸剤 ラベル</title>
<link rel="stylesheet" href="https://fonts.googleapis.com/css2?family=M+PLUS+1p:wght@500;700;800;900&family=Noto+Sans+JP:wght@400;500;700&display=swap">
<style>
  :root {
    --page: #f2f3f4;
    --label-white: #ffffff;
    --teal: #17a08a;
    --teal-dark: #0d6f66;
    --green-light: #27b38c;
    --green-deep: #0f6a5a;
    --edge-line: #7fd6bd;
    --box-edge: #8fd3c0;
    --blue-text: #1a56b8;
    --brand-yellow: #ffe36a;
    --ink: #333840;
    --rule: #9fb5b0;
  }
  * { margin: 0; padding: 0; box-sizing: border-box; }
  html, body { width: 849px; height: 1200px; overflow: hidden; }
  body {
    background: var(--page);
    font-family: "Noto Sans JP", sans-serif;
    display: flex; align-items: center; justify-content: center;
  }
  .label {
    position: relative;
    width: 620px; height: 800px;
    background: var(--label-white);
    border-radius: 10px;
    box-shadow: 0 2px 8px rgba(0,0,0,0.12);
    overflow: hidden;
  }
  .product-name {
    position: absolute; top: 34px; left: 0; right: 0;
    text-align: center;
    font-family: "M PLUS 1p", sans-serif;
    font-weight: 900; font-size: 104px; letter-spacing: 6px; line-height: 1.3;
    color: var(--teal);
    text-shadow: 2px 3px 0 var(--teal-dark);
  }
  .band {
    position: absolute; top: 180px; left: 0;
    width: 620px; height: 360px;
  }
  .effect-box {
    position: absolute; top: 246px; left: 70px;
    width: 480px; height: 220px;
    background: var(--label-white);
    border-radius: 110px;
    border: 6px solid var(--box-edge);
    display: flex; flex-direction: column; align-items: center; justify-content: center;
    font-family: "M PLUS 1p", sans-serif; font-weight: 800;
    color: var(--blue-text);
    font-size: 50px; line-height: 1.2;
    transform: rotate(-6deg);
  }
  .effect-box span { display: block; }
  .pack-bar {
    position: absolute; top: 500px; left: 250px;
    width: 330px; height: 38px;
    background: var(--green-deep);
    color: #fff;
    font-size: 21px; font-weight: 700;
    display: flex; align-items: center; justify-content: center; gap: 24px;
  }
  .pack-bar .brand { color: var(--brand-yellow); }
  .store {
    position: absolute; top: 590px; left: 0; right: 0;
    text-align: center; color: var(--ink);
  }
  .store-name { font-size: 42px; font-weight: 500; letter-spacing: 3px; }
  .store-name .branch { margin-left: 18px; }
  .store-rule { width: 480px; height: 2px; background: var(--rule); margin: 16px auto 14px; }
  .store-address { font-size: 17px; }
  .store-address .corp { margin-right: 10px; }
  .store-phone { font-size: 24px; margin-top: 6px; display: flex; align-items: center; justify-content: center; gap: 6px; }
</style>
</head>
<body>
  <div class="label">
    <h1 class="product-name">整腸剤</h1>

    <svg class="band" viewBox="0 0 620 360" role="img" aria-label="緑の帯（光が差し込むような斜めの模様）">
      <defs>
        <linearGradient id="bandFill" x1="0" y1="0" x2="1" y2="1">
          <stop offset="0" stop-color="#27b38c"/>
          <stop offset="1" stop-color="#0f6a5a"/>
        </linearGradient>
      </defs>
      <path d="M0 30 Q310 -20 620 20 L620 320 Q310 370 0 330 Z" fill="url(#bandFill)"/>
      <path d="M0 30 Q310 -20 620 20" fill="none" stroke="#7fd6bd" stroke-width="4"/>
      <path d="M0 330 Q310 370 620 320" fill="none" stroke="#7fd6bd" stroke-width="4"/>
    </svg>

    <div class="effect-box">
      <span>便秘・</span>
      <span>腹部膨満感・</span>
      <span>軟便</span>
    </div>

    <div class="pack-bar"><span class="brand">すみれ薬局製剤</span><span>16包入</span></div>

    <div class="store">
      <p class="store-name">すみれ薬局<span class="branch">北町店</span></p>
      <div class="store-rule"></div>
      <p class="store-address"><span class="corp">株式会社すみれ</span>〒310-0000 茨城県みどり市中央1-2-3</p>
      <p class="store-phone">
        <svg width="22" height="22" viewBox="0 0 24 24" aria-hidden="true"><path fill="#333840" d="M6.6 10.8a15 15 0 0 0 6.6 6.6l2.2-2.2a1 1 0 0 1 1-.25 11.4 11.4 0 0 0 3.6.6 1 1 0 0 1 1 1V20a1 1 0 0 1-1 1A17 17 0 0 1 3 4a1 1 0 0 1 1-1h3.5a1 1 0 0 1 1 1c0 1.25.2 2.45.6 3.6a1 1 0 0 1-.25 1z"/></svg>
        029-000-1234
      </p>
    </div>
  </div>
</body>
</html>
```